Banner Ad Design Project

I have a digital X Ray blog. I need a header to fit my WP theme.
Please visit the site and let me know what you think. I am open to other design ideas not only the banner. I want the to be clean and professional.

Thank you
www.CordlessPlateScan.com

Target Market(s)

Medical Doctors, Orthopedic Surgeon, X-Ray equipment Dealers,

Industry/Entity Type

Digital

```html
<!DOCTYPE html>
<html lang="en">
<head>
<meta charset="utf-8">
<title>Wireless Digital X-Ray — Flat Panel Detector</title>
<link rel="stylesheet" href="https://fonts.googleapis.com/css2?family=Open+Sans:ital,wght@0,600;0,700;1,800&display=swap">
<style>
  :root {
    --brand-blue: #1b5fa9;
    --ink-dark: #333333;
    --ink-mid: #3c3c3c;
    --paper: #ffffff;
    --tone-light: #f2f2f2;
    --tone-mid: #dcdcdc;
  }
  html, body {
    margin: 0;
    padding: 0;
    width: 1200px;
    height: 194px;
    overflow: hidden;
    background: var(--paper);
  }
  .banner {
    position: relative;
    width: 1200px;
    height: 194px;
    overflow: hidden;
    background: linear-gradient(90deg, var(--paper) 0%, var(--paper) 30%, var(--tone-light) 65%, var(--tone-mid) 100%);
    font-family: "Open Sans", Arial, sans-serif;
  }
  .banner__device {
    position: absolute;
    right: 0;
    top: 0;
    width: 760px;
    height: 194px;
  }
  .banner__copy {
    position: absolute;
    left: 0;
    top: 0;
  }
  .banner__headline {
    position: absolute;
    left: 48px;
    top: 26px;
    margin: 0;
    white-space: nowrap;
    font-size: 58px;
    font-weight: 800;
    font-style: italic;
    letter-spacing: -1px;
    line-height: 1;
    color: var(--brand-blue);
    text-shadow: 2px 2px 0 var(--paper);
  }
  .banner__product {
    position: absolute;
    left: 100px;
    top: 98px;
    margin: 0;
    white-space: nowrap;
    font-size: 31px;
    font-weight: 700;
    letter-spacing: 3.4px;
    line-height: 1;
    color: var(--ink-dark);
  }
  .banner__tagline {
    position: absolute;
    left: 65px;
    top: 138px;
    margin: 0;
    white-space: nowrap;
    font-size: 21px;
    font-weight: 600;
    letter-spacing: 0.6px;
    line-height: 1;
    color: var(--ink-mid);
  }
</style>
</head>
<body>
  <header class="banner">
    <svg class="banner__device" role="img" aria-label="Faint illustration of a wireless flat panel X-ray detector fading into the background" viewBox="0 0 760 194" preserveAspectRatio="none">
      <defs>
        <linearGradient id="deviceTone" x1="0" y1="0" x2="1" y2="1">
          <stop offset="0" stop-color="#ffffff" stop-opacity="0"/>
          <stop offset="0.5" stop-color="#ffffff" stop-opacity="0.7"/>
          <stop offset="1" stop-color="#e6e6e6" stop-opacity="0.6"/>
        </linearGradient>
      </defs>
      <rect x="0" y="0" width="760" height="194" fill="url(#deviceTone)"/>
    </svg>
    <div class="banner__copy">
      <h1 class="banner__headline">WIRELESS DIGITAL X-RAY</h1>
      <p class="banner__product">FLAT PANEL DETECTOR</p>
      <p class="banner__tagline">THE SIMPLE WAY TO UPGRADE TO DR</p>
    </div>
  </header>
</body>
</html>
```